Wedding / 60th Birthday Invitations

We need invitation design for our Wedding and Partners 60th Birthday.
We have come up with a design that reflects both ourselves and the events but needs fine tuning and we are hoping you can do this for us.
We want bridal owls sitting in a Vornelle car holding a 60th balloon.
Please see sketches attached with invite details. Colour theme is Black, Red & White.
We also require a print for the poem for Wishing Well & Acceptance Cards
Thank you

Wedding

```html
<!DOCTYPE html>
<html lang="en">
<head>
<meta charset="utf-8">
<title>60th Birthday and Marriage Party Invitation</title>
<link rel="stylesheet" href="https://fonts.googleapis.com/css2?family=Anton&family=Oswald:wght@400;500;700&family=Pathway+Gothic+One&family=PT+Sans+Narrow:wght@400;700&family=Yellowtail&display=swap">
<style>
  :root {
    --ink: #3a3a3a;
    --lime: #cfd82a;
    --lime-dark: #a9b21c;
    --paper: #ffffff;
    --paper-edge: #e2e2e2;
    --rule: #9a9a9a;
  }
  html, body {
    margin: 0;
    padding: 0;
    width: 869px;
    height: 1200px;
    overflow: hidden;
  }
  .invitation {
    position: relative;
    width: 869px;
    height: 1200px;
    background: radial-gradient(ellipse at 50% 45%, var(--paper) 55%, var(--paper-edge) 100%);
    color: var(--ink);
    overflow: hidden;
  }
  .abs { position: absolute; margin: 0; }
  .invited-to {
    left: 146px; top: 70px;
    font-family: "Pathway Gothic One", sans-serif;
    font-size: 42px;
    letter-spacing: 0.5px;
    line-height: 1;
  }
  .hosts {
    left: 104px; top: 106px;
    width: 712px; height: 84px;
    z-index: 2;
  }
  .hosts svg { display: block; width: 712px; height: 84px; overflow: visible; }
  .headline { left: 0; top: 0; width: 869px; height: 1200px; z-index: 1; }
  .owl-car {
    left: 502px; top: 330px;
    width: 326px; height: 250px;
    border-radius: 90px 90px 30px 30px;
    background: linear-gradient(180deg, #9fd8e2 0%, #f2a6cf 30%, #d6e03a 55%, #c8d12c 85%, #8a8a8a 100%);
    z-index: 1;
  }
  .gifts {
    left: 172px; width: 522px; top: 758px;
    display: flex; align-items: center; gap: 8px;
    font-family: "PT Sans Narrow", sans-serif;
    font-size: 20px;
    letter-spacing: 1px;
    line-height: 1;
    color: var(--ink);
  }
  .gifts::before, .gifts::after {
    content: ""; flex: 1; height: 1px; background: var(--ink);
  }
  .tagline {
    left: 0; right: 0; top: 797px;
    text-align: center;
    font-family: "Pathway Gothic One", sans-serif;
    font-size: 20px;
    line-height: 1;
  }
  .rule {
    left: 152px; width: 566px; height: 1px; background: var(--rule);
  }
  .rule--upper { top: 840px; }
  .rule--lower { top: 904px; }
  .when {
    left: 0; right: 0; top: 850px;
    text-align: center;
    font-family: "Pathway Gothic One", sans-serif;
    font-size: 44px;
    line-height: 1;
    word-spacing: 2px;
  }
  .when .divider { margin: 0 14px; }
  .venue-name { left: 0; top: 0; width: 869px; height: 1200px; }
  .venue-address {
    left: 0; right: 0; top: 974px;
    text-align: center;
    font-family: "Pathway Gothic One", sans-serif;
    font-size: 46px;
    line-height: 1;
    letter-spacing: 0.5px;
  }
  .transport {
    left: 60px; top: 1048px;
    display: flex; align-items: center;
    font-family: "Pathway Gothic One", sans-serif;
    font-size: 25px;
    line-height: 1;
  }
  .transport .option {
    display: inline-flex; align-items: center; margin-left: 12px;
  }
  .transport .option + .option { margin-left: 28px; }
  .check-circle {
    width: 28px; height: 28px; border: 1px solid var(--ink); border-radius: 50%;
    display: inline-block; margin-right: 1px;
  }
  .rsvp-bar {
    left: 0; top: 1094px; width: 869px; height: 42px;
    background: var(--ink);
    border-top: 2px solid var(--lime);
    border-bottom: 2px solid var(--lime);
    color: var(--paper);
    display: flex; align-items: center; justify-content: center;
    font-family: "PT Sans Narrow", sans-serif;
    font-size: 26px;
    line-height: 1;
  }
  .rsvp-bar strong { font-weight: 700; margin-left: 6px; }
</style>
</head>
<body>
<main class="invitation">
  <p class="abs invited-to">YOU ARE INVITED TO</p>
  <h1 class="abs hosts" aria-label="Della Whitford &amp; Martin Okafor">
    <svg viewBox="0 0 712 84" aria-hidden="true">
      <text x="0" y="58" font-family="Yellowtail, cursive" font-size="64" textLength="704" lengthAdjust="spacingAndGlyphs" fill="#2e2e2e">Della Whitford &amp; Martin Okafor</text>
    </svg>
  </h1>

  <svg class="abs headline" viewBox="0 0 869 1200" aria-label="60th Birthday">
    <polygon points="60,676 170,676 170,756 60,756 106,716" fill="var(--lime)"/>
    <polygon points="808,676 700,676 700,756 808,756 762,716" fill="var(--lime)"/>
    <polygon points="150,704 190,676 190,704" fill="var(--lime-dark)"/>
    <polygon points="718,704 678,676 678,704" fill="var(--lime-dark)"/>
    <rect x="150" y="704" width="568" height="78" fill="var(--lime)"/>

    <text x="80" y="566" font-family="Anton, sans-serif" font-size="422" textLength="462" lengthAdjust="spacingAndGlyphs" fill="var(--lime)" aria-hidden="true">60</text>
    <text x="90" y="556" font-family="Anton, sans-serif" font-size="422" textLength="462" lengthAdjust="spacingAndGlyphs" fill="var(--ink)">60</text>
    <text x="556" y="312" font-family="Oswald, sans-serif" font-weight="500" font-size="140" textLength="156" lengthAdjust="spacingAndGlyphs" fill="var(--ink)">TH</text>

    <text x="200" y="704" font-family="Oswald, sans-serif" font-weight="700" font-size="140" textLength="492" lengthAdjust="spacingAndGlyphs" fill="var(--ink)">BIRTHDAY</text>
    <text x="234" y="754" font-family="Oswald, sans-serif" font-weight="700" font-size="44" textLength="398" lengthAdjust="spacingAndGlyphs" fill="var(--ink)">AND MARRIAGE PARTY</text>
  </svg>

  <div class="abs owl-car" role="img" aria-label="Illustration of a bride owl and a groom owl riding in a lime green convertible car"></div>

  <p class="abs gifts">NO GIFTS PLEASE</p>
  <p class="abs tagline">Fun, Friends, Music and Dancing to Celebrate our Marriage &amp; Martin's Turning 60 Years Young!</p>

  <div class="abs rule rule--upper"></div>
  <p class="abs when">SATURDAY, 8 OCTOBER, 2016<span class="divider">|</span>BEGINS AT 5PM</p>
  <div class="abs rule rule--lower"></div>

  <svg class="abs venue-name" viewBox="0 0 869 1200" aria-label="The Grumpy Ox Brewery">
    <text x="174" y="970" font-family="Oswald, sans-serif" font-weight="700" font-size="58" textLength="520" lengthAdjust="spacingAndGlyphs" fill="var(--ink)">THE GRUMPY OX BREWERY</text>
  </svg>
  <p class="abs venue-address">418 Harlow Rd., Harlow Valley, WA</p>

  <p class="abs transport">Bus transport to venue available. Limited numbers please confirm if required.
    <span class="option"><span class="check-circle"></span>Yes</span>
    <span class="option"><span class="check-circle"></span>No</span>
  </p>

  <p class="abs rsvp-bar">RSVP by the 8th of August to Della at<strong>0491555203</strong></p>
</main>
</body>
</html>
```